Heron Freightways LLC needs a web desigh ASAP!

We need a fully functioning web site for our trucking company!
we currently have our domain and logo.
Attached you will find our logo files and word documents with info we would like to include in our web page. (Navigation Tabs and dropdown menu)
Our domain is heronfreightways.net (from webnestly)
Our Chatterbook page is Heron Freightways LLC. You can find pictures and a little bit about our company.
our original logo is the one with bull on the left side.
Our trucking company is based in south Texas, but travel within the USA and Canada.

Target Market(s)

Logistic
Refrigerated Fleet Clients
Transportation
Trucking companies

Industry/Entity Type

Trucking Company

Coding

Coded - Design and coding required

Number of Pages Required

1 page

Font styles to use
Sans Serif

Colors
f04a51
3277b5
ffffff

Requirements
Must have
• our main email contact is Info@heronfreightways.net
• we would like see the colors of our logo. it would be nice to have a truck with our logo in the background.
• We need a web site that we can manage on our own easily.
Nice to have
• roads, highways
• get a quote module
• our inspirational web pages are:
• www.marwickhaulage.com
• www.dorvelcargo.com
• we are open to use stock photos

```html
<!DOCTYPE html>
<html lang="en">
<head>
<meta charset="utf-8">
<title>Heron Freightways</title>
<link href="https://fonts.googleapis.com/css2?family=Open+Sans:wght@400;600;700;800&family=Lato:wght@400;700&display=swap" rel="stylesheet">
<style>
:root{
  --navy:#0f2240;
  --navy-deep:#0a1a33;
  --red:#b8121f;
  --red-dark:#8c0d17;
  --blue:#2f72b5;
  --ink:#2b2b2b;
  --grey-text:#555c63;
  --grey-line:#d9d9d9;
  --panel:#efefef;
  --dark:#1b2028;
  --footer:#1c2329;
  --footer-bottom:#12171c;
  --white:#ffffff;
}
*{box-sizing:border-box;margin:0;padding:0}
html,body{width:1200px;height:2473px;overflow:hidden}
body{position:relative;font-family:'Lato',Arial,sans-serif;color:var(--ink);background:var(--white)}
.abs{position:absolute}
h1,h2,h3,h4{font-family:'Open Sans',Arial,sans-serif}

/* top bar */
.topbar{left:0;top:0;width:1200px;height:43px;background:var(--navy)}
.topbar .phone-badge{left:99px;top:6px;width:31px;height:31px;border-radius:50%;background:var(--red);display:flex;align-items:center;justify-content:center}
.topbar .phone-number{left:143px;top:10px;color:var(--white);font:700 17px 'Open Sans',sans-serif}
.topbar .account{top:13px;color:var(--white);font-size:13px;display:flex;align-items:center;gap:6px}
.topbar .search{left:730px;top:6px;width:196px;height:32px;border-radius:16px;background:var(--white);font-size:12px;color:#777;padding:8px 14px}
.topbar .search-btn{right:3px;top:3px;width:26px;height:26px;border-radius:50%;background:var(--red);display:flex;align-items:center;justify-content:center}
.quote-cta{left:943px;top:0;width:158px;height:49px;background:var(--red);color:var(--white);font:700 14px 'Open Sans',sans-serif;display:flex;align-items:center;justify-content:center;border-radius:0 0 3px 3px}

/* header */
.header{left:0;top:43px;width:1200px;height:114px;background:linear-gradient(#ffffff,#ececec)}
.brand{left:99px;top:38px;display:flex;align-items:center;gap:12px;font:800 32px 'Open Sans',sans-serif;color:var(--navy)}
.brand .dot{width:34px;height:34px;border-radius:50%;background:var(--red)}
.nav{top:48px;font:400 15px 'Open Sans',sans-serif;color:#333}
.nav.active{color:var(--red);font-weight:700;font-style:italic}

/* hero */
.hero{left:0;top:157px;width:1200px;height:514px;background:linear-gradient(180deg,#5d6c70 0%,#c7834a 28%,#e49a4d 42%,#8d8a58 62%,#5c7d38 80%,#3f5e2a 100%)}
.hero h1{left:97px;top:360px;color:var(--white);font-weight:600;font-size:35px;line-height:45px;letter-spacing:.5px}
.hero .dots{left:575px;top:616px;display:flex;gap:6px}
.hero .dots span{width:8px;height:8px;border-radius:50%;background:var(--white)}
.hero .dots span.off{background:transparent;border:1px solid var(--white)}

/* services */
.section-title{width:1200px;left:0;text-align:center;font-weight:600;font-size:32px;color:#2b2b2b}
.section-title em{font-style:normal;color:var(--blue)}
.service-card{width:357px;height:161px;background:var(--white);border:1px solid #e2e2e2;box-shadow:0 1px 4px rgba(0,0,0,.12);padding:20px 24px 0 52px}
.service-card h3{font-weight:700;font-size:19px;color:var(--navy)}
.service-card .rule{width:83px;height:3px;background:var(--red);margin:10px 0 12px}
.service-card p{font-size:13.5px;line-height:25px;color:var(--grey-text)}
.service-card .corner{position:absolute;right:0;bottom:0;width:0;height:0;border-left:28px solid transparent;border-bottom:28px solid var(--red)}
.service-card .plus{position:absolute;right:4px;bottom:2px;color:var(--white);font:700 12px 'Open Sans',sans-serif}
.service-icon{width:114px;height:114px;border-radius:50%;background:var(--white);border:3px solid var(--red);box-shadow:0 0 0 5px #f1f1f1;display:flex;align-items:center;justify-content:center}
.btn{display:flex;align-items:stretch;height:29px;border-radius:4px;overflow:hidden;color:var(--white);font:700 13px 'Open Sans',sans-serif}
.btn .label{background:var(--red);display:flex;align-items:center;justify-content:center}
.btn .arrow{background:var(--red-dark);width:26px;display:flex;align-items:center;justify-content:center}

/* welcome */
.welcome{left:0;top:1302px;width:1200px;height:481px;background:var(--dark)}
.welcome h2{color:var(--white)}
.welcome .intro{left:99px;top:1430px;width:523px;color:var(--white);font-size:15px;line-height:27.6px}
.video{left:695px;top:1450px;width:385px;height:269px;border:6px solid #d8d8d8;background:linear-gradient(135deg,#c9c3b0 0%,#7d7f7a 40%,#2e3134 70%,#6f8a7c 100%)}
.video .play{left:160px;top:102px;width:52px;height:52px;border-radius:50%;background:var(--red);display:flex;align-items:center;justify-content:center}

/* jobs + quote */
.jobs-quote{left:0;top:1783px;width:1200px;height:368px;background:var(--panel)}
.block-title{font-weight:600;font-size:32px;color:var(--navy)}
.block-title em{font-style:normal;color:var(--blue)}
.title-rule{height:2px;background:var(--grey-line)}
.title-rule::before{content:"";display:block;width:46px;height:3px;background:var(--red)}
.divider{left:600px;top:1826px;width:1px;height:300px;background:#d4d4d4}
.tab{top:1898px;font:600 18px 'Open Sans',sans-serif;display:flex;align-items:center;gap:12px}
.tab .bullet{width:6px;height:6px;border-radius:50%}
.job-text{left:102px;font-size:13.5px;color:var(--ink);line-height:21px}
.duty{left:102px;font-size:13.5px;display:flex;align-items:center;gap:10px}
.field{background:var(--white);border:1px solid #cfcfcf;font-size:12.5px;color:#666;padding:11px 10px}
.submit{left:634px;top:2050px;width:111px;height:38px;background:var(--red);color:var(--white);font-size:14px;display:flex;align-items:center;justify-content:center}

/* footer */
.footer{left:0;top:2151px;width:1200px;height:268px;background:var(--footer)}
.footer h4{font-weight:700;font-size:19px;color:var(--white);padding-bottom:8px;border-bottom:1px solid #3a444e}
.footer .links{list-style:none;font-size:12px;color:var(--white);line-height:27.5px}
.contact-line{color:var(--white);font-size:12px;display:flex;align-items:center;gap:12px}
.address-box{left:350px;top:2230px;width:181px;height:53px;background:#0f1317;color:var(--white);font-size:11px;line-height:14px;padding:5px 9px}
.address-box strong{font-size:12px}
.map{left:575px;top:2233px;width:264px;height:154px;background:linear-gradient(135deg,#ececec,#d8d8d8);border:3px solid #f4f4f4}
.newsletter-input{left:887px;top:2263px;width:214px;height:30px;background:var(--white);border-radius:3px;font-size:12px;color:#444;padding:8px 12px}
.subscribe{left:887px;top:2307px;width:91px;height:28px;background:var(--red);color:var(--white);font:700 11px 'Open Sans',sans-serif;display:flex;align-items:center;justify-content:center}
.bottom-bar{left:0;top:2419px;width:1200px;height:54px;background:var(--footer-bottom);color:var(--white);font-size:12px}
.social{width:27px;height:27px;border-radius:50%;background:#6b737b}
</style>
</head>
<body>

<!-- top bar -->
<div class="abs topbar">
  <div class="abs phone-badge">
    <svg width="15" height="15" viewBox="0 0 24 24"><path fill="#fff" d="M6.6 10.8a15 15 0 0 0 6.6 6.6l2.2-2.2c.3-.3.7-.4 1-.2 1.1.4 2.3.6 3.6.6.6 0 1 .4 1 1V20c0 .6-.4 1-1 1A17 17 0 0 1 3 4c0-.6.4-1 1-1h3.5c.6 0 1 .4 1 1 0 1.3.2 2.5.6 3.6.1.3 0 .7-.2 1z"/></svg>
  </div>
  <div class="abs phone-number">1-800-555-0142</div>
  <div class="abs account" style="left:565px">
    <svg width="12" height="14" viewBox="0 0 12 14"><rect x="1" y="6" width="10" height="8" rx="1" fill="#fff"/><path d="M3 6V4a3 3 0 0 1 6 0v2" stroke="#fff" stroke-width="1.8" fill="none"/></svg>Login
  </div>
  <div class="abs" style="left:627px;top:13px;width:1px;height:17px;background:#51607a"></div>
  <div class="abs account" style="left:640px">
    <svg width="14" height="14" viewBox="0 0 14 14"><circle cx="10" cy="4" r="3.2" fill="#fff"/><path d="M8 6 2 12" stroke="#fff" stroke-width="2.4"/></svg>Register
  </div>
  <div class="abs search">Search
    <div class="abs search-btn">
      <svg width="13" height="13" viewBox="0 0 13 13"><circle cx="5.5" cy="5.5" r="4" stroke="#fff" stroke-width="1.8" fill="none"/><path d="M8.5 8.5 12 12" stroke="#fff" stroke-width="1.8"/></svg>
    </div>
  </div>
</div>
<div class="abs quote-cta">GET A FREE QUOTE</div>

<!-- header -->
<header class="abs header">
  <div class="abs brand"><span class="dot"></span>Heron Freightways</div>
  <nav>
    <span class="abs nav active" style="left:532px">Home</span>
    <span class="abs nav" style="left:634px">About Us</span>
    <span class="abs nav" style="left:756px">Services</span>
    <span class="abs nav" style="left:870px">Job Openings</span>
    <span class="abs nav" style="left:1022px">Contact Us</span>
  </nav>
</header>

<!-- hero -->
<section class="abs hero" role="img" aria-label="Photo of a white lorry driving along a highway at sunset between green fields">
  <h1 class="abs" style="top:203px">PROVIDING FIRST CLASS<br>TRANSPORTATION<br>SERVICES</h1>
  <div class="abs dots" style="top:459px"><span class="off"></span><span></span><span></span><span></span></div>
</section>

<!-- services -->
<h2 class="abs section-title" style="top:710px">Our <em>Services</em></h2>

<div class="abs service-card" style="left:197px;top:811px">
  <h3>Transport of Packaged Goods</h3><div class="rule"></div>
  <p>Lorem ipsum dolor sit amet, consectetuer adipiscing elit, sed diam nonummy nibh euismod tincidunt ut laoreet dolore....</p>
  <span class="corner"></span><span class="plus">+</span>
</div>
<div class="abs service-icon" style="left:127px;top:835px">
  <svg width="66" height="46" viewBox="0 0 66 46" fill="#6b6b6b"><rect x="2" y="14" width="20" height="22"/><rect x="24" y="8" width="16" height="28"/><rect x="40" y="2" width="4" height="36"/><rect x="44" y="30" width="20" height="4"/><circle cx="10" cy="40" r="5"/><circle cx="32" cy="40" r="5"/></svg>
</div>

<div class="abs service-card" style="left:686px;top:811px">
  <h3>National Road Transport</h3><div class="rule"></div>
  <p>Lorem ipsum dolor sit amet, consectetuer adipiscing elit, sed diam nonummy nibh euismod tincidunt ut laoreet dolore....</p>
  <span class="corner"></span><span class="plus">+</span>
</div>
<div class="abs service-icon" style="left:616px;top:835px">
  <svg width="70" height="44" viewBox="0 0 70 44" fill="#6b6b6b"><rect x="24" y="2" width="44" height="30"/><path d="M2 18 10 10h12v22H2z"/><circle cx="12" cy="37" r="5"/><circle cx="40" cy="37" r="5"/><circle cx="56" cy="37" r="5"/></svg>
</div>

<div class="abs service-card" style="left:197px;top:1015px">
  <h3>Warehousing and Storage</h3><div class="rule"></div>
  <p>Lorem ipsum dolor sit amet, consectetuer adipiscing elit, sed diam nonummy nibh euismod tincidunt ut laoreet dolore....</p>
  <span class="corner"></span><span class="plus">+</span>
</div>
<div class="abs service-icon" style="left:127px;top:1039px">
  <svg width="52" height="52" viewBox="0 0 52 52" fill="#6b6b6b"><path d="M4 14 26 2l22 12v36H4z"/><rect x="14" y="22" width="24" height="4" fill="#fff"/><rect x="14" y="30" width="24" height="4" fill="#fff"/><rect x="14" y="38" width="24" height="4" fill="#fff"/></svg>
</div>

<div class="abs service-card" style="left:686px;top:1015px">
  <h3>Forwarding Services</h3><div class="rule"></div>
  <p>Lorem ipsum dolor sit amet, consectetuer adipiscing elit, sed diam nonummy nibh euismod tincidunt ut laoreet dolore....</p>
  <span class="corner"></span><span class="plus">+</span>
</div>
<div class="abs service-icon" style="left:616px;top:1039px">
  <svg width="58" height="52" viewBox="0 0 58 52" fill="#6b6b6b"><path d="M6 14 29 2l23 12z"/><rect x="4" y="16" width="50" height="32"/><g fill="#fff"><rect x="10" y="20" width="3" height="24"/><rect x="18" y="20" width="3" height="24"/><rect x="26" y="20" width="3" height="24"/><rect x="34" y="20" width="3" height="24"/><rect x="42" y="20" width="3" height="24"/></g></svg>
</div>

<div class="abs btn" style="left:539px;top:1221px;width:122px">
  <span class="label" style="flex:1">View All</span>
  <span class="arrow"><svg width="8" height="12" viewBox="0 0 8 12"><path d="M1 1l5 5-5 5" stroke="#fff" stroke-width="2" fill="none"/></svg></span>
</div>

<!-- welcome -->
<section class="abs welcome">
  <h2 class="abs section-title" style="top:40px;color:#fff">Welcome to Heron Freightways</h2>
</section>
<p class="abs intro" style="left:99px;top:1430px;width:523px;color:#fff;font-size:15px;line-height:27.6px">Lorem ipsum dolor sit amet, consectetuer adipiscing elit, sed diam mmy ibh euismod tincidunt ut laoreet dolore magna aliquam erat volutpat. Ut wisi im ad minim veniam, quis nostrud exerci tation ullamcorper suscipit lobortis nisl ut aliquip ex ea commodo consequat. Duis autem vel eum iriure dolor in hendrerit in vulputate velit esse molestie consequat, vel illum dolore eu feugiat nulla facilisis at vero eros et accumsan et iusto odio dignissim qui blandit praesent luptatum zzril delenit augue duis dolore, &nbsp;Lorem ipsum dolor sit amet, consectetuer adipiscing elit,</p>
<div class="abs btn" style="left:99px;top:1673px;width:121px">
  <span class="label" style="flex:1">Read More</span>
  <span class="arrow"><svg width="8" height="12" viewBox="0 0 8 12"><path d="M1 1l5 5-5 5" stroke="#fff" stroke-width="2" fill="none"/></svg></span>
</div>
<div class="abs video" role="img" aria-label="Video still of a dark lorry with a white trailer driving on a road">
  <div class="abs play"><svg width="18" height="20" viewBox="0 0 18 20"><path d="M2 1l15 9-15 9z" fill="#fff"/></svg></div>
</div>

<!-- jobs and quote -->
<section class="abs jobs-quote"></section>
<h2 class="abs block-title" style="left:97px;top:1815px">Job <em>Openings</em></h2>
<div class="abs title-rule" style="left:99px;top:1872px;width:468px"></div>
<div class="abs tab" style="left:103px;color:var(--red)"><span class="bullet" style="background:var(--red)"></span>Drivers</div>
<div class="abs tab" style="left:232px;color:var(--ink)"><span class="bullet" style="background:#c4c4c4"></span>Office Clerk</div>
<p class="abs job-text" style="top:1932px;width:460px">We are currently hiring CDL Truck Drivers. Must have 2 year minimum experience and a clean driving record.</p>
<p class="abs job-text" style="top:1985px">Duties and responsibilities:</p>
<div class="abs duty" style="top:2016px"><svg width="16" height="8" viewBox="0 0 16 8"><path d="M0 4h14M10 1l4 3-4 3" stroke="#333" stroke-width="1.5" fill="none"/></svg>Loading and unloading goods</div>
<div class="abs duty" style="top:2049px"><svg width="16" height="8" viewBox="0 0 16 8"><path d="M0 4h14M10 1l4 3-4 3" stroke="#333" stroke-width="1.5" fill="none"/></svg>Follow rules of Department of Transportation</div>
<div class="abs duty" style="top:2082px"><svg width="16" height="8" viewBox="0 0 16 8"><path d="M0 4h14M10 1l4 3-4 3" stroke="#333" stroke-width="1.5" fill="none"/></svg>Understanding the route of their shipment</div>

<div class="abs divider"></div>

<h2 class="abs block-title" style="left:633px;top:1815px">Get A <em>Quote</em></h2>
<div class="abs title-rule" style="left:636px;top:1872px;width:465px"></div>
<div class="abs field" style="left:634px;top:1902px;width:228px;height:38px">Name</div>
<div class="abs field" style="left:634px;top:1948px;width:228px;height:38px">Email</div>
<div class="abs field" style="left:634px;top:1996px;width:228px;height:38px">Phone</div>
<div class="abs field" style="left:872px;top:1902px;width:229px;height:132px">Message</div>
<div class="abs submit">Submit</div>

<!-- footer -->
<footer class="abs footer">
  <div class="abs" style="left:99px;top:28px;width:114px"><h4>Quick Links</h4></div>
  <ul class="abs links" style="left:99px;top:72px">
    <li>Home</li><li>About Us</li><li>Services</li><li>Job Openings</li><li>Contact Us</li>
  </ul>
  <div class="abs" style="left:259px;top:28px;width:272px"><h4>Contact Info</h4></div>
  <div class="abs" style="left:575px;top:28px;width:264px"><h4>Location Map</h4></div>
  <div class="abs" style="left:887px;top:28px;width:214px"><h4>Newsletter Sign Up</h4></div>
  <p class="abs" style="left:887px;top:80px;color:#fff;font-size:12px">Stay updated with latest news from</p>
</footer>
<svg class="abs" style="left:327px;top:2232px" width="16" height="22" viewBox="0 0 16 22"><path d="M8 0a8 8 0 0 1 8 8c0 6-8 14-8 14S0 14 0 8a8 8 0 0 1 8-8z" fill="#fff"/><circle cx="8" cy="8" r="3" fill="#1c2329"/></svg>
<div class="abs address-box"><strong>Heron Freightways</strong><br>Loream Ipsum, Dollar smit, ACT Wendmoor - 0123989.</div>
<div class="abs contact-line" style="left:327px;top:2306px"><svg width="16" height="16" viewBox="0 0 24 24"><path fill="#fff" d="M6.6 10.8a15 15 0 0 0 6.6 6.6l2.2-2.2c.3-.3.7-.4 1-.2 1.1.4 2.3.6 3.6.6.6 0 1 .4 1 1V20c0 .6-.4 1-1 1A17 17 0 0 1 3 4c0-.6.4-1 1-1h3.5c.6 0 1 .4 1 1 0 1.3.2 2.5.6 3.6.1.3 0 .7-.2 1z"/></svg><strong>555 010 7788</strong></div>
<div class="abs contact-line" style="left:327px;top:2349px"><svg width="16" height="12" viewBox="0 0 16 12"><rect x="1" y="1" width="14" height="10" fill="none" stroke="#fff" stroke-width="1.5"/><path d="M1 1l7 6 7-6" stroke="#fff" stroke-width="1.5" fill="none"/></svg>info@heronfreightways.net</div>
<div class="abs map" role="img" aria-label="Street map showing the company location on Larkspur Lane">
  <svg class="abs" style="left:40px;top:48px" width="16" height="22" viewBox="0 0 16 22"><path d="M8 0a8 8 0 0 1 8 8c0 6-8 14-8 14S0 14 0 8a8 8 0 0 1 8-8z" fill="#d7262c"/><circle cx="8" cy="8" r="3" fill="#fff"/></svg>
  <span class="abs" style="left:58px;top:66px;font-size:10px;font-weight:700;color:var(--red)">14 Larkspur Lane</span>
</div>
<div class="abs newsletter-input">
  <svg style="vertical-align:-2px;margin-right:8px" width="14" height="10" viewBox="0 0 16 12"><rect x="1" y="1" width="14" height="10" fill="none" stroke="#777" stroke-width="1.5"/><path d="M1 1l7 6 7-6" stroke="#777" stroke-width="1.5" fill="none"/></svg>Enter your Email
</div>
<div class="abs subscribe">SUBSCRIBE</div>

<div class="abs bottom-bar">
  <span class="abs" style="left:99px;top:20px">Copyright © 2016 Heron Freightways. All Right Reserved</span>
  <span class="abs" style="left:918px;top:20px">Follow Us :</span>
  <span class="abs social" style="left:992px;top:13px"></span>
  <span class="abs social" style="left:1030px;top:13px"></span>
  <span class="abs social" style="left:1070px;top:13px"></span>
</div>

</body>
</html>
```